8 1/2 x 11 Flyer Design for Water Damage Restoration Company

Houston Texas based Water Damage Restoration company is needing a advertising flyer that highlights water damage and water extraction.

KESTRAL Emergency Services
52710 Harlow Crossing Suite G4
Houston, Texas 77193
713-846-5170
www.KESTRAL58129.example

Water Damage Restoration
Water Extraction
Mold Prevention
24/7/365
FREE Evaluations

Suggested photos to use:
Water Damage
Leaking Pipes
Water on floors and ground
Water pouring from ceilings
Technicians
Company Logo
Photos

Company Colors:
Orange and Blue

```html
<!DOCTYPE html>
<html lang="en">
<head>
<meta charset="utf-8">
<title>KESTRAL Emergency Services – Water Damage Restoration Flyer</title>
<link href="https://fonts.googleapis.com/css2?family=Bebas+Neue&family=Mulish:wght@400;600&display=swap" rel="stylesheet">
<style>
  :root {
    --bg-dark: #2a292b;
    --grid-line: rgba(255,255,255,0.035);
    --orange: #f7941d;
    --orange-red: #ef4e2a;
    --white: #ffffff;
    --ink: #1c1c1c;
    --blue-deep: #0d3aa8;
    --blue-bright: #00c8ee;
    --brand-blue: #1aa6e4;
    --body-text: #e8e8e8;
  }
  * { margin: 0; padding: 0; box-sizing: border-box; }
  html, body { width: 927px; height: 1200px; overflow: hidden; background: var(--bg-dark); }
  .flyer {
    position: relative; width: 927px; height: 1200px; overflow: hidden;
    background-color: var(--bg-dark);
    background-image:
      linear-gradient(var(--grid-line) 1px, transparent 1px),
      linear-gradient(90deg, var(--grid-line) 1px, transparent 1px);
    background-size: 24px 24px;
    font-family: "Bebas Neue", "Oswald", sans-serif;
    color: var(--white);
  }
  .abs { position: absolute; }

  /* Brand tab */
  .brand-tab {
    left: 37px; top: 0; width: 133px; height: 113px;
    background: linear-gradient(180deg, var(--brand-blue) 0%, var(--brand-blue) 35%, #c9a58e 100%);
    clip-path: polygon(0 0, 100% 0, 100% 76%, 50% 100%, 0 76%);
    display: flex; flex-direction: column; align-items: center; padding-top: 30px;
  }
  .brand-name {
    font-family: "Bebas Neue", sans-serif; color: #0f3f8f;
    font-size: 25px; line-height: 1; letter-spacing: 1px; text-align: center;
  }
  .brand-name small { display: block; font-size: 10.5px; letter-spacing: 0.5px; }

  /* Contact */
  .contact-icon { left: 680px; top: 15px; width: 49px; height: 50px; background: var(--orange); display: flex; align-items: center; justify-content: center; }
  .contact-label { left: 739px; top: 11px; font-size: 36px; line-height: 1; color: var(--orange); letter-spacing: 0.5px; }
  .contact-phone { left: 739px; top: 43px; font-family: "Mulish", sans-serif; font-size: 21px; line-height: 1; color: var(--white); }

  /* Headline */
  .headline-pre { left: 0; width: 927px; top: 108px; text-align: center; font-size: 50px; line-height: 1; letter-spacing: 2px; }
  .headline-main {
    left: 0; width: 927px; top: 153px; text-align: center; font-size: 112px; line-height: 1; letter-spacing: 1px;
    background: linear-gradient(90deg, var(--orange-red) 0%, var(--orange) 100%);
    -webkit-background-clip: text; background-clip: text; color: transparent;
  }
  .headline-box {
    left: 240px; top: 271px; width: 448px; height: 52px; background: var(--white);
    color: var(--ink); font-size: 40px; line-height: 54px; text-align: center; letter-spacing: 2px;
  }

  /* Photo band */
  .photo-band { left: 0; top: 356px; width: 927px; height: 491px; overflow: hidden; }
  .photo-fill { position: absolute; inset: 0; background: linear-gradient(110deg, #c7cfd9 0%, #e6e9ee 60%, #8896b0 100%); }
  .photo-tint-left { position: absolute; inset: 0; background: linear-gradient(160deg, var(--blue-deep) 0%, #0a7fd8 40%, var(--blue-bright) 100%); clip-path: polygon(0 0, 40.5% 0, 67% 100%, 0 100%); opacity: 0.95; }
  .photo-tint-right { position: absolute; inset: 0; background: linear-gradient(160deg, #0b3fc0, #1a2f80); clip-path: polygon(79% 0, 100% 0, 100% 62%); opacity: 0.85; }
  .offer { left: 73px; top: 440px; }
  .offer-big { font-size: 170px; line-height: 0.73; letter-spacing: 4px; display: block; }
  .offer-small { font-size: 60px; line-height: 1; letter-spacing: 2px; display: block; margin-top: 8px; }
  .offer-rule { width: 302px; height: 6px; background: var(--white); margin-top: 10px; }

  /* Services */
  .services-title { left: 0; width: 927px; top: 858px; text-align: center; font-size: 94px; line-height: 1; color: var(--orange); }
  .service { top: 986px; text-align: center; }
  .service-head { display: flex; align-items: center; justify-content: center; gap: 6px; font-size: 30px; line-height: 1; color: var(--orange); white-space: nowrap; }
  .service-icon { flex: none; width: 24px; height: 24px; background: var(--orange); display: flex; align-items: center; justify-content: center; }
  .service-text { font-family: "Mulish", sans-serif; font-size: 11.6px; line-height: 18px; color: var(--body-text); margin-top: 9px; }
  .divider { top: 983px; width: 3px; height: 121px; background: var(--white); }

  /* Footer */
  .footer-band { left: 0; top: 1146px; width: 927px; height: 54px; background: linear-gradient(90deg, var(--orange) 0%, var(--orange-red) 100%); text-align: center; font-family: "Mulish", sans-serif; font-size: 19px; letter-spacing: 7px; line-height: 54px; color: var(--white); }
</style>
</head>
<body>
<main class="flyer">

  <svg class="abs decor" width="927" height="1200" viewBox="0 0 927 1200" style="left:0;top:0">
    <defs>
      <linearGradient id="stripeOrange" x1="0" y1="0" x2="1" y2="1">
        <stop offset="0" stop-color="#f7941d"/><stop offset="1" stop-color="#ef6a2a"/>
      </linearGradient>
    </defs>
    <g fill="#ffffff">
      <circle cx="382" cy="17" r="2.5"/><circle cx="414" cy="17" r="2.5"/><circle cx="446" cy="17" r="2.5"/><circle cx="478" cy="17" r="2.5"/><circle cx="510" cy="17" r="2.5"/><circle cx="542" cy="17" r="2.5"/>
      <circle cx="8" cy="323" r="2.5"/><circle cx="40" cy="323" r="2.5"/><circle cx="72" cy="323" r="2.5"/><circle cx="104" cy="323" r="2.5"/><circle cx="136" cy="323" r="2.5"/><circle cx="168" cy="323" r="2.5"/>
      <circle cx="8" cy="341" r="2.5"/><circle cx="40" cy="341" r="2.5"/><circle cx="72" cy="341" r="2.5"/><circle cx="104" cy="341" r="2.5"/><circle cx="136" cy="341" r="2.5"/>
      <circle cx="784" cy="862" r="2.5"/><circle cx="816" cy="862" r="2.5"/><circle cx="848" cy="862" r="2.5"/><circle cx="880" cy="862" r="2.5"/><circle cx="912" cy="862" r="2.5"/>
      <circle cx="752" cy="880" r="2.5"/><circle cx="784" cy="880" r="2.5"/><circle cx="816" cy="880" r="2.5"/><circle cx="848" cy="880" r="2.5"/><circle cx="880" cy="880" r="2.5"/><circle cx="912" cy="880" r="2.5"/>
    </g>
    <g fill="none" stroke="#f7c51d" stroke-width="1.6">
      <circle cx="312" cy="60" r="6"/><circle cx="776" cy="270" r="6"/><circle cx="20" cy="1091" r="6"/>
      <circle cx="105" cy="913" r="12" stroke-width="3"/>
    </g>
    <g fill="#f7941d">
      <rect x="793" y="123" width="33" height="6"/><rect x="806" y="110" width="6" height="33"/>
      <rect x="58" y="220" width="46" height="7"/><rect x="78" y="200" width="7" height="46"/>
      <rect x="878" y="948" width="40" height="7"/><rect x="895" y="932" width="7" height="40"/>
    </g>
  </svg>

  <div class="abs brand-tab">
    <div class="brand-name">KESTRAL<small>EMERGENCY SERVICES</small></div>
  </div>

  <div class="abs contact-icon">
    <svg width="28" height="28" viewBox="0 0 24 24"><path fill="#1c1c1c" d="M6.6 10.8a15.1 15.1 0 0 0 6.6 6.6l2.2-2.2a1 1 0 0 1 1-.25 11.4 11.4 0 0 0 3.6.57 1 1 0 0 1 1 1V20a1 1 0 0 1-1 1A17 17 0 0 1 3 4a1 1 0 0 1 1-1h3.5a1 1 0 0 1 1 1c0 1.250.2 2.450.57 3.57a1 1 0 0 1-.25 1z"/></svg>
  </div>
  <div class="abs contact-label">CONTACT US:</div>
  <div class="abs contact-phone">713-846-5170</div>

  <h1>
    <span class="abs headline-pre">PROFESSIONAL</span>
    <span class="abs headline-main">WATER DAMAGE</span>
    <span class="abs headline-box">RESTORATION</span>
  </h1>

  <section class="abs photo-band" role="img" aria-label="Technician in gloves tightening a sink drain pipe with an orange wrench">
    <div class="photo-fill"></div>
    <div class="photo-tint-left"></div>
    <div class="photo-tint-right"></div>
  </section>

  <svg class="abs stripes" width="927" height="1200" viewBox="0 0 927 1200" style="left:0;top:0">
    <g fill="url(#stripeOrange)">
      <polygon points="890,194 927,231 927,262 890,225"/>
      <polygon points="890,246 927,283 927,314 890,277"/>
      <polygon points="890,298 927,335 927,357 890,329"/>
      <polygon points="0,836 42,878 42,908 0,866"/>
      <polygon points="0,888 42,930 42,960 0,918"/>
      <polygon points="0,940 42,982 42,1012 0,970"/>
    </g>
    <g fill="#2a292b">
      <polygon points="890,357 927,394 927,425 890,388"/>
      <polygon points="890,409 927,446 927,477 890,440"/>
      <polygon points="0,732 42,774 42,804 0,762"/>
      <polygon points="0,784 42,826 42,847 0,814"/>
    </g>
  </svg>

  <div class="abs offer">
    <span class="offer-big">WITH</span>
    <span class="offer-big">FREE</span>
    <span class="offer-small">CONSULTATION</span>
    <div class="offer-rule"></div>
  </div>

  <h2 class="abs services-title">OUR SERVICES</h2>

  <article class="abs service" style="left:70px;width:258px">
    <div class="service-head"><span class="service-icon"><svg width="16" height="16" viewBox="0 0 16 16"><circle cx="8" cy="8" r="5" fill="none" stroke="#2a292b" stroke-width="3" stroke-dasharray="2.5 1.4"/></svg></span>DAMAGE RESTORATION</div>
    <p class="service-text">Restore homes and buildings affected by water damage caused by floods, leaks, or other related incidents. The process involves removing excess water and drying out the affected areas.</p>
  </article>
  <div class="abs divider" style="left:339px"></div>

  <article class="abs service" style="left:360px;width:256px">
    <div class="service-head"><span class="service-icon"><svg width="16" height="16" viewBox="0 0 16 16"><path fill="#2a292b" d="M3 14V8h3v6zM7 9h6v2H7zM5 3a2 2 0 1 1 0 .01z"/></svg></span>WATER EXTRACTION</div>
    <p class="service-text">Removes standing water from a property before it can cause further damage.</p>
  </article>
  <div class="abs divider" style="left:628px"></div>

  <article class="abs service" style="left:648px;width:256px">
    <div class="service-head"><span class="service-icon"><svg width="16" height="16" viewBox="0 0 16 16"><circle cx="8" cy="8" r="4" fill="#2a292b"/><path stroke="#2a292b" stroke-width="1.5" d="M8 1v3M8 12v3M1 8h3M12 8h3"/></svg></span>MOLD PREVENTION</div>
    <p class="service-text">Prevent the growth of mold in areas that have been affected by water damage, using specialized equipment and techniques to mitigate the risk of mold growth.</p>
  </article>

  <footer class="abs footer-band">WWW.KESTRAL58129.EXAMPLE</footer>
</main>
</body>
</html>
```